International Business Development Firm, in need of Branded Stationery material

We just made our Logo and now we are looking for branded stationery for our company such as:

* A Letterhead with our company's name, address, and logo at the top in Word format for easy editing
* A more formal letter format with a light background design (watermark) featuring our logo, allowing us to write over it for various documents and presentations
* Business card + Envelopes are a plus but not a must
* PowerPoint for company and product introductions
* An Info sheet with Bullet Points

The design should be professional.
Please ensure the design is high quality and print ready.

Target Market(s)

Businesses and high net value individuels

Industry/Entity Type

International Business Development Firm

Colors

Designer to choose colors to be used in the design.

Requirements
Must have
• word docs so i can use the stationery templates afterwards

```html
<!DOCTYPE html>
<html lang="en">
<head>
<meta charset="utf-8">
<title>Corvale Capital — Stationery Board</title>
<link rel="stylesheet" href="https://fonts.googleapis.com/css2?family=Montserrat:wght@400;600;700&family=Open+Sans:wght@400;600&display=swap">
<style>
:root{
  --purple:#6b3f8f;
  --lilac:#9a7bb7;
  --ink:#2d2d2d;
  --grey:#8a8a8a;
  --board:#cbcbcb;
  --header:#262626;
  --paper:#ffffff;
  --panel:#e9e9ec;
}
*{margin:0;padding:0;box-sizing:border-box}
html,body{width:799px;height:1200px;overflow:hidden;background:var(--board);font-family:"Open Sans",sans-serif;color:var(--ink)}
.board{position:relative;width:799px;height:1200px}
.topbar{position:absolute;left:0;top:0;width:799px;height:80px;background:var(--header);display:flex;align-items:center;justify-content:center}
.brand{font-family:"Montserrat",sans-serif;font-weight:600;color:var(--purple);letter-spacing:.04em;white-space:nowrap;display:flex;align-items:center;gap:.35em}
.brand::before{content:"";width:.7em;height:.7em;border-radius:50%;background:currentColor;flex:none}
.brand.light{color:#fff}
.label{position:absolute;font-size:5.5px;color:#555}
.sheet{position:absolute;background:var(--paper);box-shadow:1px 2px 4px rgba(0,0,0,.25);overflow:hidden}
.band{position:absolute;background:var(--lilac);color:#fff}
.contact{font-size:4px;color:#555;display:flex;align-items:center;gap:3px;margin-bottom:3px}
.ico{width:5px;height:5px;background:var(--purple);border-radius:1px;flex:none}
.band .contact{color:#fff}
.band .ico{background:#fff}
.name{font-family:"Montserrat",sans-serif;font-weight:700;color:var(--purple)}
.role{color:#555}
.body-text{font-size:5.6px;line-height:1.55;color:#9a9a9a;text-align:justify}
.slide{position:absolute;width:225px;height:127px;background:#fff;box-shadow:1px 2px 4px rgba(0,0,0,.25);overflow:hidden}
.slide-title{position:absolute;left:7px;top:7px;font-family:"Montserrat",sans-serif;font-weight:600;font-size:7px;color:var(--ink)}
.slide-title::after{content:"";display:block;width:10px;height:1.2px;background:var(--lilac);margin-top:2px}
.slide .brand{position:absolute;right:8px;top:7px;font-size:3.6px}
.slide-foot{position:absolute;left:7px;right:14px;bottom:7px;height:.6px;background:var(--lilac)}
.tiny{font-size:2.8px;line-height:1.4;color:#777}
.sub{font-family:"Montserrat",sans-serif;font-weight:600;font-size:4px;color:var(--purple)}
.num{display:inline-flex;width:8px;height:8px;background:var(--purple);color:#fff;font-size:5px;font-weight:700;align-items:center;justify-content:center;font-family:"Montserrat",sans-serif}
.row{display:flex;gap:4px;align-items:flex-start}
</style>
</head>
<body>
<div class="board">

  <header class="topbar"><span class="brand light" style="font-size:15px">CORVALE CAPITAL</span></header>

  <!-- Business card front -->
  <span class="label" style="left:52px;top:106px">Bcard Front</span>
  <section class="sheet card-front" style="left:52px;top:116px;width:170px;height:102px">
    <span class="brand" style="position:absolute;left:12px;top:18px;font-size:6.5px">CORVALE CAPITAL</span>
    <div style="position:absolute;right:10px;top:15px;text-align:right">
      <div class="name" style="font-size:5.6px">DANIEL R. WHITCOMBE</div>
      <div class="role" style="font-size:4.2px">Managing Director</div>
    </div>
    <div class="contact" style="position:absolute;left:12px;top:55px"><span class="ico"></span>1720 Harbor Crest Avenue<br>Arlington, VA 22201</div>
    <div class="band" style="left:0;top:68px;width:108px;height:24px;clip-path:polygon(0 0,100% 0,94% 100%,0 100%);padding:3px 12px">
      <div class="contact"><span class="ico"></span>+00 987 654 32</div>
      <div class="contact"><span class="ico"></span>office@corvalecapital.com</div>
      <div class="contact"><span class="ico"></span>www.corvalecapital.com</div>
    </div>
  </section>

  <!-- Business card back -->
  <span class="label" style="left:240px;top:106px">Bcard Back</span>
  <section class="sheet card-back" style="left:240px;top:116px;width:170px;height:102px;background:var(--purple);display:flex;align-items:center;justify-content:center">
    <span class="brand light" style="font-size:9px">CORVALE CAPITAL</span>
  </section>

  <!-- Email signature -->
  <span class="label" style="left:52px;top:228px">Email Signature</span>
  <section class="sheet email-signature" style="left:52px;top:237px;width:357px;height:91px">
    <span class="brand" style="position:absolute;left:10px;top:42px;font-size:7px">CORVALE CAPITAL</span>
    <div style="position:absolute;left:83px;top:12px">
      <div class="name" style="font-size:6.2px">DANIEL R. WHITCOMBE</div>
      <div class="role" style="font-size:4.8px;border-bottom:.6px solid var(--lilac);padding-bottom:2px;width:48px">Managing Director</div>
      <div style="margin-top:6px">
        <div class="contact" style="font-size:4.4px"><span class="ico"></span>1720 Harbor Crest Avenue<br>Arlington, VA 22201</div>
        <div class="contact" style="font-size:4.4px;margin-top:6px"><span class="ico"></span>+00 987 654 32</div>
        <div class="contact" style="font-size:4.4px;margin-top:5px"><span class="ico"></span>office@corvalecapital.com</div>
        <div class="contact" style="font-size:4.4px;margin-top:5px"><span class="ico"></span>www.corvalecapital.com</div>
      </div>
    </div>
    <div class="band" style="left:0;bottom:0;width:300px;height:3px;clip-path:polygon(0 0,99% 0,100% 100%,0 100%)"></div>
  </section>

  <!-- Letterhead -->
  <span class="label" style="left:437px;top:106px">LetterHead</span>
  <div style="position:absolute;left:456px;top:133px;width:291px;height:407px;background:var(--purple);box-shadow:1px 2px 4px rgba(0,0,0,.25)"></div>
  <section class="sheet letterhead" style="left:437px;top:116px;width:292px;height:409px">
    <span class="brand" style="position:absolute;left:24px;top:30px;font-size:11px">CORVALE CAPITAL</span>
    <div style="position:absolute;left:206px;top:28px">
      <div class="contact" style="font-size:4.3px"><span class="ico"></span>+00 987 654 32</div>
      <div class="contact" style="font-size:4.3px"><span class="ico"></span>office@corvalecapital.com</div>
      <div class="contact" style="font-size:4.3px"><span class="ico"></span>www.corvalecapital.com</div>
    </div>
    <div style="position:absolute;left:22px;right:22px;top:63px;height:.6px;background:#ccc"></div>
    <div style="position:absolute;left:23px;top:98px">
      <div class="name" style="font-size:8px;color:var(--purple)">CLARA JENSEN</div>
      <div style="font-size:5px;color:#999;line-height:1.75;margin-top:2px">0198-765-432<br>clara@jensenmail.com<br>88 Linden Row, Suite 4<br>Austin, TX 7300</div>
    </div>
    <div style="position:absolute;right:23px;top:155px;font-size:5.6px;color:#888">12 December, 2024</div>
    <div style="position:absolute;left:23px;right:23px;top:168px">
      <p class="body-text">Lorem ipsum dolor sit amet, consectetuer adipiscing elit, sed diam nonummy nibh euismod tincidunt ut laoreet dolore magna aliquam erat volutpat. Ut wisi enim ad minim veniam, quis nostrud exerci tation ullamcorper suscipit lobortis nisl ut aliquip ex ea commodo consequat. Duis autem vel eum iriure dolor in hendrerit in vulputate velit esse molestie consequat, vel illum dolore eu feugiat nulla facilisis at vero eros et accumsan et iusto odio dignissim qui blandit praesent luptatum zzril delenit augue duis dolore te feugait nulla facilisi.</p>
      <p class="body-text" style="margin-top:8px">Lorem ipsum dolor sit amet, cons ectetuer adipiscing elit, sed diam nonummy nibh euismod tincidunt ut laoreet dolore magna aliquam erat volutpat. Ut wisi enim ad minim veniam, quis nostrud exerci tation ullamcorper suscipit lobortis nisl ut aliquip ex ea commodo consequat.</p>
    </div>
    <div style="position:absolute;left:24px;top:292px;font-family:Montserrat,sans-serif;font-size:6.2px;color:#444">Mr. Daniel R. Whitcombe</div>
    <div role="img" aria-label="Handwritten signature" style="position:absolute;left:38px;top:305px;width:46px;height:26px;background:linear-gradient(90deg,#f2f2f2,#e4e4e4)"></div>
    <div class="band" style="left:0;top:362px;width:200px;height:10px;clip-path:polygon(0 0,97% 0,100% 100%,0 100%);font-size:4.3px;letter-spacing:.08em;padding:2px 0 0 24px;display:flex;gap:3px;align-items:center"><span class="ico" style="background:#fff;width:4px;height:4px"></span>1720 Harbor Crest Avenue Arlington, VA 22201</div>
  </section>

  <!-- Envelope front -->
  <span class="label" style="left:52px;top:553px">Envelope</span>
  <section class="sheet envelope-front" style="left:52px;top:565px;width:340px;height:171px">
    <span class="brand" style="position:absolute;left:12px;top:22px;font-size:10px">CORVALE CAPITAL</span>
    <div class="band" style="left:0;top:147px;width:255px;height:10px;clip-path:polygon(0 0,97% 0,100% 100%,0 100%);font-size:4.3px;letter-spacing:.08em;padding-left:12px;display:flex;gap:3px;align-items:center"><span class="ico" style="background:#fff;width:4px;height:4px"></span>1720 Harbor Crest Avenue Arlington, VA 22201</div>
  </section>

  <!-- Envelope back -->
  <section class="sheet envelope-back" style="left:408px;top:565px;width:340px;height:171px">
    <div class="band" style="left:0;top:0;width:340px;height:41px;clip-path:polygon(0 0,100% 0,94% 78%,88% 100%,12% 100%,6% 78%);display:flex;justify-content:center;padding-top:10px">
      <span class="brand light" style="font-size:10px">CORVALE CAPITAL</span>
    </div>
  </section>

  <!-- Presentation -->
  <span class="label" style="left:52px;top:749px">PPT Template</span>

  <!-- Slide 1 cover -->
  <section class="slide" style="left:52px;top:759px">
    <div style="position:absolute;right:0;top:0;width:60px;height:127px;background:var(--purple);clip-path:polygon(0 0,100% 0,100% 100%,25% 100%,35% 65%)"></div>
    <span class="brand" style="position:absolute;left:14px;top:20px;font-size:8.5px">CORVALE CAPITAL</span>
    <div style="position:absolute;left:14px;top:61px;font-family:Montserrat,sans-serif;line-height:1.05">
      <div style="font-size:7.5px;color:var(--lilac)">Company</div>
      <div style="font-size:12.5px;font-weight:700;color:var(--ink)">Business</div>
      <div style="font-size:10px;font-weight:600;color:var(--lilac)">Marketing</div>
      <div style="font-size:3px;color:#999;font-style:italic;margin-top:4px;width:95px">Short note on the team and what we offer each client.</div>
    </div>
    <div style="position:absolute;left:14px;top:113px;display:flex;gap:2px"><i style="width:3px;height:3px;border-radius:50%;background:var(--lilac)"></i><i style="width:3px;height:3px;border-radius:50%;background:var(--lilac)"></i><i style="width:3px;height:3px;border-radius:50%;background:var(--purple)"></i></div>
  </section>

  <!-- Slide 2 agenda -->
  <section class="slide" style="left:288px;top:759px">
    <span class="brand">CORVALE CAPITAL</span>
    <div style="position:absolute;left:24px;top:51px;border-left:3px solid var(--lilac);padding-left:5px;font-family:Montserrat,sans-serif;font-weight:700;font-size:14px">Agenda</div>
    <div style="position:absolute;left:107px;top:32px;width:90px">
      <div class="sub">1. Lorem ipsum</div><div class="tiny" style="margin-bottom:8px">Lorem ipsum dolor sit amet, sed diam nibh</div>
      <div class="sub">2. Lorem ipsum</div><div class="tiny" style="margin-bottom:8px">Lorem ipsum dolor sit amet, sed diam nibh</div>
      <div class="sub">3. Lorem ipsum</div><div class="tiny" style="margin-bottom:8px">Lorem ipsum dolor sit amet, sed diam nibh</div>
      <div class="sub">4. Lorem ipsum</div><div class="tiny">Lorem ipsum dolor sit amet, sed diam nibh</div>
    </div>
    <div class="slide-foot"></div>
  </section>

  <!-- Slide 3 list + panel -->
  <section class="slide" style="left:523px;top:759px">
    <div class="slide-title">Text Added Hare</div><span class="brand">CORVALE CAPITAL</span>
    <div style="position:absolute;left:22px;top:30px;width:82px">
      <div class="sub">01. Aliquam Erat Volutpat</div><div class="tiny" style="margin-bottom:7px">Lorem ipsum dolor sit amet, sed diam nibh</div>
      <div class="sub">02. Consectetuer Elit</div><div class="tiny" style="margin-bottom:7px">Lorem ipsum dolor sit amet, sed diam nibh</div>
      <div class="sub">03. Duis Autem Vel Eum</div><div class="tiny" style="margin-bottom:7px">Lorem ipsum dolor sit amet, sed diam nibh</div>
      <div class="sub">04. Aliquam Erat Volutpat</div><div class="tiny">Lorem ipsum dolor sit amet, sed diam nibh</div>
    </div>
    <div style="position:absolute;left:120px;top:26px;width:78px;height:80px;background:var(--panel)"></div>
    <div style="position:absolute;left:112px;top:35px">
      <div class="row" style="margin-bottom:9px"><i style="width:12px;height:12px;border-radius:50%;background:var(--purple)"></i><div><div class="sub">Lorem ipsum</div><div class="tiny" style="width:50px">Ipsum dolor sit amet nibh</div></div></div>
      <div class="row" style="margin-bottom:9px"><i style="width:12px;height:12px;border-radius:50%;background:var(--purple)"></i><div><div class="sub">Lorem ipsum</div><div class="tiny" style="width:50px">Ipsum dolor sit amet nibh</div></div></div>
      <div class="row"><i style="width:12px;height:12px;border-radius:50%;background:var(--purple)"></i><div><div class="sub">Lorem ipsum</div><div class="tiny" style="width:50px">Ipsum dolor sit amet nibh</div></div></div>
    </div>
    <div class="slide-foot"></div>
  </section>

  <!-- Slide 4 two columns -->
  <section class="slide" style="left:52px;top:900px">
    <div class="slide-title">Text Added Hare</div><span class="brand">CORVALE CAPITAL</span>
    <div style="position:absolute;left:25px;top:28px;width:82px">
      <div class="sub" style="color:var(--ink)">1. Text Added Here</div>
      <div class="tiny">Lorem ipsum dolor sit amet, cons ectetuer adipiscing elit, sed diam nonummy nibh euismod tincidunt.</div>
      <div class="row" style="margin-top:12px"><span class="num">1.</span><div><div class="sub" style="color:var(--ink)">Lorem ipsum</div><div class="tiny">Dolor sit amet, sed diam</div></div></div>
      <div class="row" style="margin-top:8px"><span class="num" style="background:var(--lilac)">2.</span><div><div class="sub" style="color:var(--ink)">Lorem ipsum</div><div class="tiny">Dolor sit amet, sed diam</div></div></div>
    </div>
    <div style="position:absolute;left:118px;top:28px;width:82px">
      <div class="sub" style="color:var(--ink)">2. Text Added Here</div>
      <div class="tiny">Lorem ipsum dolor sit amet, cons ectetuer adipiscing elit, sed diam nonummy nibh euismod tincidunt.</div>
      <div class="row" style="margin-top:12px"><span class="num" style="background:var(--lilac)">1.</span><div><div class="sub" style="color:var(--ink)">Lorem ipsum</div><div class="tiny">Dolor sit amet, sed diam</div></div></div>
      <div class="row" style="margin-top:8px"><span class="num">2.</span><div><div class="sub" style="color:var(--ink)">Lorem ipsum</div><div class="tiny">Dolor sit amet, sed diam</div></div></div>
    </div>
    <div class="slide-foot"></div>
  </section>

  <!-- Slide 5 process boxes -->
  <section class="slide" style="left:288px;top:900px">
    <div class="slide-title">Text Added Hare</div><span class="brand">CORVALE CAPITAL</span>
    <svg style="position:absolute;left:38px;top:30px" width="150" height="56" viewBox="0 0 150 56" fill="none" stroke="#2d2d2d" stroke-width="1.4">
      <rect x="2" y="2" width="38" height="52" rx="4"/><rect x="56" y="2" width="38" height="52" rx="4"/><rect x="110" y="2" width="38" height="52" rx="4"/>
      <circle cx="40" cy="15" r="2" fill="#2d2d2d"/><circle cx="56" cy="41" r="2" fill="#2d2d2d"/><circle cx="94" cy="15" r="2" fill="#2d2d2d"/><circle cx="110" cy="41" r="2" fill="#2d2d2d"/>
    </svg>
    <div style="position:absolute;left:42px;top:48px;width:34px;text-align:center"><div class="sub" style="font-size:3.4px">IDEA</div><div class="tiny">Lorem ipsum dolor sit amet</div></div>
    <div style="position:absolute;left:96px;top:48px;width:34px;text-align:center"><div class="sub" style="font-size:3.4px">PROMOTION</div><div class="tiny">Lorem ipsum dolor sit amet</div></div>
    <div style="position:absolute;left:150px;top:48px;width:34px;text-align:center"><div class="sub" style="font-size:3.4px">GROWTH</div><div class="tiny">Lorem ipsum dolor sit amet</div></div>
    <div class="tiny" style="position:absolute;left:28px;right:28px;top:95px;text-align:center">Lorem ipsum dolor sit amet, consectetuer adipiscing elit, sed diam nonummy nibh euismod tincidunt ut laoreet dolore.</div>
    <div class="slide-foot"></div>
  </section>

  <!-- Slide 6 text + bullet panel -->
  <section class="slide" style="left:523px;top:900px">
    <div class="slide-title">Text Added Hare</div><span class="brand">CORVALE CAPITAL</span>
    <div style="position:absolute;left:16px;top:28px;width:88px">
      <div class="sub">1. Text Added Here</div>
      <div class="tiny">Lorem ipsum dolor sit amet, cons ectetuer adipiscing elit, sed diam nonummy nibh euismod tincidunt ut laoreet dolore magna aliquam erat volutpat.</div>
      <div class="sub" style="margin-top:8px">2. Text Added Here</div>
      <div class="tiny">Lorem ipsum dolor sit amet, cons ectetuer adipiscing elit, sed diam nonummy nibh euismod tincidunt ut laoreet dolore magna aliquam erat volutpat.</div>
    </div>
    <div style="position:absolute;left:111px;top:28px;width:98px;height:72px;background:var(--lilac);padding:8px 6px;color:#fff;font-size:3px;line-height:1.4">
      <p style="margin-bottom:9px">• Lorem ipsum dolor sit amet, cons nonummy nibh euismod tincidunt</p>
      <p style="margin-bottom:9px">• Lorem ipsum dolor sit amet, cons nonummy nibh euismod tincidunt</p>
      <p>• Lorem ipsum dolor sit amet, cons nonummy nibh euismod tincidunt</p>
    </div>
    <div class="slide-foot"></div>
  </section>

  <!-- Slide 7 devices -->
  <section class="slide" style="left:52px;top:1038px">
    <div class="slide-title">Text Added Hare</div><span class="brand">CORVALE CAPITAL</span>
    <div style="position:absolute;left:14px;top:26px;width:66px">
      <div class="tiny">Lorem ipsum dolor sit amet, consectetuer adipiscing elit, sed diam nonummy nibh euismod tincidunt ut laoreet dolore magna aliquam erat volutpat.</div>
      <div class="row" style="margin-top:16px"><span class="num">1.</span><div><div class="sub" style="color:var(--ink)">Lorem ipsum</div><div class="tiny">Dolor sit amet, sed diam</div></div></div>
      <div class="row" style="margin-top:5px"><span class="num">2.</span><div><div class="sub" style="color:var(--ink)">Lorem ipsum</div><div class="tiny">Dolor sit amet, sed diam</div></div></div>
      <div class="row" style="margin-top:5px"><span class="num">3.</span><div><div class="sub" style="color:var(--ink)">Lorem ipsum</div><div class="tiny">Dolor sit amet, sed diam</div></div></div>
    </div>
    <div role="img" aria-label="Three phone screens showing service steps" style="position:absolute;left:98px;top:18px;width:100px;height:92px;background:linear-gradient(135deg,#f1f1f3,#e2e2e6)"></div>
    <div class="slide-foot"></div>
  </section>

  <!-- Slide 8 cycle chart -->
  <section class="slide" style="left:288px;top:1038px">
    <div class="slide-title">Text Added Hare</div><span class="brand">CORVALE CAPITAL</span>
    <svg style="position:absolute;left:82px;top:34px" width="62" height="62" viewBox="0 0 62 62">
      <path d="M31 1A30 30 0 0 1 61 31H46A15 15 0 0 0 31 16Z" fill="#9a7bb7"/>
      <path d="M61 31A30 30 0 0 1 31 61V46A15 15 0 0 0 46 31Z" fill="#6b3f8f"/>
      <path d="M31 61A30 30 0 0 1 1 31H16A15 15 0 0 0 31 46Z" fill="#9a7bb7"/>
      <path d="M1 31A30 30 0 0 1 31 1V16A15 15 0 0 0 16 31Z" fill="#6b3f8f"/>
      <circle cx="31" cy="31" r="15" fill="#fff"/>
    </svg>
    <div style="position:absolute;left:99px;top:58px;width:28px;text-align:center;font-family:Montserrat,sans-serif;font-weight:700;font-size:5px;line-height:1.1">Text Added</div>
    <div style="position:absolute;left:20px;top:36px;width:58px;text-align:right"><div class="sub" style="color:var(--ink)">Text Here</div><div class="tiny">Lorem ipsum dolor sit amet, sed diam</div></div>
    <div style="position:absolute;left:150px;top:36px;width:58px"><div class="sub" style="color:var(--ink)">Text Here</div><div class="tiny">Lorem ipsum dolor sit amet, sed diam</div></div>
    <div style="position:absolute;left:20px;top:80px;width:58px;text-align:right"><div class="sub" style="color:var(--ink)">Text Here</div><div class="tiny">Lorem ipsum dolor sit amet, sed diam</div></div>
    <div style="position:absolute;left:150px;top:80px;width:58px"><div class="sub" style="color:var(--ink)">Text Here</div><div class="tiny">Lorem ipsum dolor sit amet, sed diam</div></div>
    <div class="slide-foot"></div>
  </section>

  <!-- Slide 9 thank you -->
  <section class="slide" style="left:523px;top:1038px;background:var(--purple);color:#fff">
    <div style="position:absolute;left:108px;top:26px;font-family:Montserrat,sans-serif;font-weight:700;font-size:16px">Thank You</div>
    <div style="position:absolute;left:108px;top:52px;font-size:4.4px;line-height:1.3">
      <div class="row" style="margin-bottom:6px"><span class="ico" style="background:#fff;width:6px;height:6px;margin-right:2px"></span><div style="border-left:.6px solid #fff;padding-left:3px">+18 3345 2210 7765<br>+18 3345 2210 7766</div></div>
      <div class="row" style="margin-bottom:6px"><span class="ico" style="background:#fff;width:6px;height:6px;margin-right:2px"></span><div style="border-left:.6px solid #fff;padding-left:3px">www.corvalecapital.com<br>team@corvalecapital.com</div></div>
      <div class="row"><span class="ico" style="background:#fff;width:6px;height:6px;margin-right:2px"></span><div style="border-left:.6px solid #fff;padding-left:3px">1720 Harbor Crest Avenue,<br>Arlington, VA 22201</div></div>
    </div>
  </section>

</div>
</body>
</html>
```